Morden, Creative, Unique, Independent Wine Shop

1. We are a brand new wine shop located in Melbourne Australia, we have our logo already, simply use the logo to design a business card.
2. I have uploaded our logo in two versions, with or without shadow, any of them is acceptable.
3. Make it as creative and unique as possible, no limitation of shape, color combination, geometry pattern, fonts, composing etc.
3. Info on the card:
- Brambleford Wine Cellar (Not very necessary if logo is obviously shown)
- 42 Ferncastle Steet, Hampton, Victoria, Australia 3188
- +61 3 9018 4637
- www.bramblefordwinecellar.com.au
- bramblefordwinecellar@mailvista.com
- Additional icons: Google, Instagram, Facebook, Twitter
4. Once again, forget it is a commercial card, make it special.

```html
<!DOCTYPE html>
<html lang="en">
<head>
<meta charset="utf-8">
<title>Brambleford Wine Cellar — Business Card</title>
<link href="https://fonts.googleapis.com/css2?family=Roboto:wght@300;400;500&display=swap" rel="stylesheet">
<style>
  :root {
    --crimson: #a81c3f;
    --crimson-deep: #a51d41;
    --crimson-soft: #b43a58;
    --slate: #666666;
    --ink: #5a5a5a;
    --paper: #ffffff;
    --backdrop: #e6e6e6;
  }
  * { box-sizing: border-box; margin: 0; padding: 0; }
  html, body {
    width: 1125px; height: 1200px; overflow: hidden;
    background: var(--backdrop);
    font-family: "Roboto", Arial, sans-serif;
  }
  .card {
    position: absolute; left: 150px; width: 825px; height: 472px;
    border-radius: 22px; overflow: hidden;
  }
  .card--front { top: 98px; background: var(--paper); }
  .card--back { top: 631px; background: var(--crimson-deep); }

  /* Front */
  .brand {
    position: absolute; left: 57px; top: 66px; width: 340px;
    color: var(--crimson); font-weight: 400; font-size: 34px;
    letter-spacing: 2px; line-height: 1.15; text-transform: uppercase;
  }
  .mark-spot {
    position: absolute; right: 14px; top: 120px;
    width: 210px; height: 210px; border-radius: 50%;
    background: var(--slate);
  }
  .person { position: absolute; left: 57px; top: 205px; }
  .person__name { color: var(--crimson); font-weight: 500; font-size: 29px; }
  .person__role { color: var(--ink); font-weight: 300; font-size: 22px; margin-top: 4px; }

  .address {
    position: absolute; left: 57px; top: 290px;
    color: var(--ink); font-weight: 300; font-size: 18px; line-height: 24px;
    font-style: normal;
  }
  .contacts {
    position: absolute; left: 57px; top: 360px; list-style: none;
    color: var(--ink); font-weight: 300; font-size: 18px; line-height: 24px;
  }
  .contacts li { display: flex; align-items: center; gap: 9px; }
  .contacts svg { width: 13px; height: 13px; fill: var(--crimson); flex: none; }
  .contacts .accent { color: var(--crimson); }

  .social {
    position: absolute; left: 485px; top: 402px; display: flex; gap: 4px;
  }
  .social__link {
    width: 19px; height: 19px; border-radius: 4px; background: var(--crimson);
    display: flex; align-items: center; justify-content: center;
  }
  .social__link svg { width: 11px; height: 11px; fill: none; stroke: var(--paper); stroke-width: 2.4; stroke-linecap: round; }

  /* Back */
  .back-pattern {
    position: absolute; inset: 0;
    background: linear-gradient(180deg, var(--crimson-deep), var(--crimson-soft) 50%, var(--crimson-deep));
    opacity: 0.6;
  }
  .back-lockup {
    position: absolute; left: 175px; top: 150px;
    display: flex; align-items: center; gap: 28px;
  }
  .back-lockup__spot {
    width: 110px; height: 110px; border-radius: 50%; background: var(--paper); flex: none;
  }
  .back-lockup__name {
    color: var(--paper); font-weight: 400; font-size: 44px;
    letter-spacing: 3px; line-height: 1.12; text-transform: uppercase;
  }
</style>
</head>
<body>
  <section class="card card--front" aria-label="Business card front">
    <div class="brand">Brambleford Wine Cellar</div>
    <div class="mark-spot" aria-hidden="true"></div>

    <div class="person">
      <h1 class="person__name">Marcus Hale</h1>
      <p class="person__role">Manager</p>
    </div>

    <address class="address">
      42 Ferncastle Steet, Hampton<br>
      Victoria, Australia 3188
    </address>

    <ul class="contacts">
      <li>
        <svg viewBox="0 0 24 24"><path d="M6.6 10.8a15.1 15.1 0 0 0 6.6 6.6l2.2-2.2c.3-.3.7-.4 1-.2 1.1.4 2.3.6 3.6.6.6 0 1 .4 1 1V20c0 .6-.4 1-1 1A17 17 0 0 1 3 4c0-.6.4-1 1-1h3.5c.6 0 1 .4 1 1 0 1.3.2 2.5.6 3.6.1.3 0 .7-.2 1z"/></svg>
        +61 3 9018 4637
      </li>
      <li>
        <svg viewBox="0 0 24 24"><path d="M2 5h20v14H2zm2 2v.5l8 5 8-5V7l-8 5z"/></svg>
        bramblefordwinecellar@mailvista.com
      </li>
      <li>
        <svg viewBox="0 0 24 24"><circle cx="12" cy="12" r="10"/></svg>
        <span>www.<span class="accent">bramblefordwinecellar</span>.com.au</span>
      </li>
    </ul>

    <div class="social" aria-label="Social media links">
      <span class="social__link"><svg viewBox="0 0 12 12"><path d="M3 9l6-6M4.5 3H9v4.5"/></svg></span>
      <span class="social__link"><svg viewBox="0 0 12 12"><path d="M3 9l6-6M4.5 3H9v4.5"/></svg></span>
      <span class="social__link"><svg viewBox="0 0 12 12"><path d="M3 9l6-6M4.5 3H9v4.5"/></svg></span>
      <span class="social__link"><svg viewBox="0 0 12 12"><path d="M3 9l6-6M4.5 3H9v4.5"/></svg></span>
    </div>
  </section>

  <section class="card card--back" aria-label="Business card back">
    <div class="back-pattern" role="img" aria-label="Repeating tone-on-tone pattern of the brand emblem on crimson"></div>
    <div class="back-lockup">
      <div class="back-lockup__spot" aria-hidden="true"></div>
      <div class="back-lockup__name">Brambleford<br>Wine Cellar</div>
    </div>
  </section>
</body>
</html>
```